Business Card Design for Bright Easel Designs

I need a business card design for Artist Marlon Teague who specializes in Digital Fine Art, Digital Illustration, Murals and Mixed Media. Digital art techniques combine the use of a computer and specialized programs coupled with the same methods and theories used to produce traditional art. The final design should use the new logo that was just deigned and reflect an artist who has embraced the evolution of art by using modern technology to paint vibrant, stunning and high quality art. Please make this a double sided card and use the attached photo on the back of the card. Please include the name of the business: Bright Easel Designs, Artist: Marlon Teague, Phone: 555-872-3096 Website: brighteaseldesigns.example

Target Market(s)

Anyone looking for fine art for there home or business.

Industry/Entity Type

Computer

Contact Information for Business Card

This should be a double sided business card with a modern feel to it.

Font styles to use
Sans Serif

Requirements
Must have
• Artist Name: Marlon Teague
• Business Name and Logo: Bright Easel Designs
• Phone: 555-872-3096
• Website: brighteaseldesigns.example
• specializes in Digital Fine Art, Digital Illustration, Murals and Mixed Media
Nice to have
• Black background with new logo that is attached to file

```html
<!DOCTYPE html>
<html lang="en">
<head>
<meta charset="utf-8">
<title>Bright Easel Designs — Business Card</title>
<link rel="stylesheet" href="https://fonts.googleapis.com/css2?family=Oswald:wght@300;400&display=swap">
<style>
  :root {
    --backdrop: #b0e0cc;
    --card-black: #0b0b0b;
    --rule: #3a3a3a;
    --label-grey: #6f6f6f;
    --value-white: #f2f2f2;
    --brand-blue: #5b7de0;
    --koi-gold: #e0a620;
    --koi-teal: #4fc8c0;
    --koi-red: #d2452e;
  }
  * { box-sizing: border-box; margin: 0; padding: 0; }
  html, body {
    width: 1200px; height: 904px; overflow: hidden;
    background: var(--backdrop);
    font-family: "Oswald", "Arial Narrow", sans-serif;
  }
  .sheet {
    width: 1200px; height: 904px;
    display: flex; align-items: center; justify-content: center; gap: 60px;
  }
  .card {
    width: 525px; height: 300px;
    background: var(--card-black);
    position: relative;
    box-shadow: 0 18px 40px rgba(0,0,0,.25);
    overflow: hidden;
  }

  /* Front side */
  .card-front .brand {
    position: absolute; left: 0; top: 0; width: 200px; height: 230px;
    display: flex; align-items: center; justify-content: center; gap: 8px;
  }
  .brand-dot { width: 10px; height: 10px; border-radius: 50%; background: var(--brand-blue); }
  .brand-name {
    color: var(--brand-blue); font-weight: 400; font-size: 17px;
    letter-spacing: .04em; text-transform: uppercase;
  }
  .divider-v {
    position: absolute; left: 200px; top: 28px; width: 1px; height: 190px;
    background: var(--rule);
  }
  .divider-h {
    position: absolute; left: 200px; top: 120px; width: 300px; height: 1px;
    background: var(--rule);
  }
  .contact {
    position: absolute; left: 222px; top: 40px; right: 20px;
    display: grid; grid-template-columns: 88px 1fr; row-gap: 30px;
    font-size: 14px; letter-spacing: .06em; text-transform: uppercase;
  }
  .contact .label { color: var(--label-grey); font-weight: 300; }
  .contact .value { color: var(--value-white); font-weight: 400; }
  .contact .value.web { text-transform: none; }
  .specialties {
    position: absolute; left: 0; right: 0; bottom: 34px;
    text-align: center; color: var(--label-grey);
    font-size: 11px; font-weight: 300; letter-spacing: .08em; text-transform: uppercase;
  }

  /* Back side */
  .card-back .artwork {
    position: absolute; inset: 22px 60px;
    border-radius: 40% 50% 45% 40%;
    background:
      radial-gradient(circle at 70% 35%, var(--koi-red) 0%, transparent 35%),
      radial-gradient(circle at 40% 60%, var(--koi-gold) 0%, transparent 55%),
      radial-gradient(circle at 50% 50%, var(--koi-teal) 0%, transparent 75%);
  }
</style>
</head>
<body>
  <main class="sheet">
    <section class="card card-front" aria-label="Card front">
      <div class="brand">
        <span class="brand-dot"></span>
        <span class="brand-name">Bright Easel Designs</span>
      </div>
      <div class="divider-v"></div>
      <div class="divider-h"></div>
      <div class="contact">
        <span class="label">Artist Name</span><span class="value">Marlon Teague</span>
        <span class="label">Phone</span><span class="value">555-872-3096</span>
        <span class="label">Website</span><span class="value web">brighteaseldesigns.example</span>
      </div>
      <p class="specialties">Specializing in Digital Fine Art, Digital Illustration, Murals and Mixed Media</p>
    </section>

    <section class="card card-back" aria-label="Card back">
      <div class="artwork" role="img" aria-label="Colourful illustration of a golden koi fish leaping through stylised teal waves"></div>
    </section>
  </main>
</body>
</html>
```